Simple : A Therapist is looking for a Design

Im lookind for a business card design for my new business .
my therapy field - Attuned Somatic Release .
Its part of Osteopatic medicine .
its gental, not invasive method that focus on the bones of the skull (cranial) .
i want some kind of skull in it like the attached photo.

Target Market(s)

people that suffer from pain

Industry/Entity Type

Physical Therapy

Contact Information for Business Card

i want people to understand this is diffrent kind of therapy
its anatomy base , gental and give outstanding result .

Font styles to use
Serif

Colors
fee18a
cadf82
fbc994
cedeed
fbe7d2
fff3d1

Requirements
Must have
• one side: my name (Eliran Tsabari) ,
• phone number ( 0541762908)
• email (tsabarieliran@mailvent.net)
• other side : Attuned Somatic Release
Nice to have
• i want some kind of skull in it like the attached photo.
• very powrful, accurate and smart.
• nice colores (maybe lite orange?, lite green?) , simple, relax, smart

```html
<!DOCTYPE html>
<html lang="en">
<head>
<meta charset="utf-8">
<title>Attuned Somatic Release – Business Card</title>
<link href="https://fonts.googleapis.com/css2?family=Didact+Gothic&family=Montserrat:wght@700&display=swap" rel="stylesheet">
<style>
  :root {
    --backdrop: #d9d9d9;
    --card-orange: #e4a263;
    --pattern-tone: #d8955a;
    --card-cream: #efe5cf;
    --accent-orange: #d9853a;
    --ink: #1f1f1f;
    --white: #ffffff;
  }
  html, body {
    margin: 0;
    width: 1200px;
    height: 1200px;
    overflow: hidden;
    background: var(--backdrop);
  }
  .canvas {
    position: relative;
    width: 1200px;
    height: 1200px;
  }
  .card {
    position: absolute;
    left: 180px;
    width: 840px;
    height: 480px;
    box-shadow: 0 6px 18px rgba(0,0,0,0.12);
    overflow: hidden;
  }
  .card--front {
    top: 80px;
    background: var(--card-orange);
  }
  .card--back {
    top: 640px;
    background: var(--card-cream);
  }
  .front-pattern {
    position: absolute;
    inset: 0;
    background: radial-gradient(circle at 55% 50%, var(--pattern-tone) 0%, var(--card-orange) 70%);
    opacity: 0.7;
  }
  .brand {
    position: absolute;
    left: 110px;
    top: 170px;
    display: flex;
    align-items: center;
    gap: 26px;
  }
  .brand-circle {
    width: 120px;
    height: 120px;
    border: 4px solid var(--white);
    border-radius: 50%;
    box-sizing: border-box;
    flex: none;
  }
  .brand-name {
    margin: 0;
    font-family: "Didact Gothic", sans-serif;
    font-weight: 400;
    font-size: 58px;
    line-height: 1.05;
    color: var(--white);
  }
  .back-mark {
    position: absolute;
    right: 70px;
    top: 50px;
    width: 140px;
    height: 140px;
    border: 4px solid var(--accent-orange);
    border-radius: 50%;
    box-sizing: border-box;
  }
  .contact {
    position: absolute;
    left: 60px;
    bottom: 60px;
  }
  .contact-name {
    margin: 0 0 14px;
    font-family: "Montserrat", sans-serif;
    font-weight: 700;
    font-size: 40px;
    color: var(--ink);
  }
  .contact-line {
    display: flex;
    align-items: center;
    gap: 22px;
    margin: 6px 0;
    font-family: "Didact Gothic", sans-serif;
    font-size: 30px;
    color: var(--ink);
  }
  .contact-icon {
    width: 36px;
    height: 30px;
    flex: none;
  }
</style>
</head>
<body>
<main class="canvas">
  <section class="card card--front" aria-label="Card front">
    <div class="front-pattern" role="img" aria-label="Faint decorative pattern of interlocking circles and leaf shapes"></div>
    <div class="brand">
      <span class="brand-circle"></span>
      <h1 class="brand-name">Attuned<br>Somatic Release</h1>
    </div>
  </section>

  <section class="card card--back" aria-label="Card back">
    <span class="back-mark"></span>
    <div class="contact">
      <h2 class="contact-name">Eliran Tsabari</h2>
      <p class="contact-line">
        <svg class="contact-icon" viewBox="0 0 36 30" aria-hidden="true">
          <path d="M6 4 L12 4 L15 11 L11 14 Q15 21 22 24 L25 20 L32 23 L32 28 Q18 29 10 20 Q4 13 6 4 Z" fill="none" stroke="var(--accent-orange)" stroke-width="2" stroke-linejoin="round"/>
        </svg>
        0541762908
      </p>
      <p class="contact-line">
        <svg class="contact-icon" viewBox="0 0 36 30" aria-hidden="true">
          <rect x="3" y="5" width="30" height="20" fill="none" stroke="var(--accent-orange)" stroke-width="2"/>
          <path d="M3 5 L18 17 L33 5 M3 25 L14 14 M33 25 L22 14" fill="none" stroke="var(--accent-orange)" stroke-width="2"/>
        </svg>
        tsabarieliran@mailvent.net
      </p>
    </div>
  </section>
</main>
</body>
</html>
```